Business Card Design for high end dental office

Please include attached logo with office name in the font selected for business card design. Emphasis will be on elegance, simplicity with a modern look. We are a high end boutique dental office that focuses on customer service and expertise of our doctors.

The current font chosen for the letters is Garamond, but we are open to suggestions.

The main theme color for the office is cyan and silver.

Target Market(s)

Oral health/esthetics driven adults of the Los Angeles area aged 25 to 80 with above average median household income. Customers range from young professionals such doctors, lawyers, engineers, or entrepreneurs to retired senior citizens.

Industry/Entity Type

Boutique

Colors

Designer to choose colors to be used in the design.

Requirements
Must have
• Business logo and name
Doctor's name and degrees: Marcus Dorval, DDS, MMSc
Doctor's field of work: Smile Solutions/Prosthodontics/Implant Dentistry
Nice to have
• Rounded business card corners.
Background or watermark of logo.
Matte cyan with shiny silver color.
Textured feel.

Files

```html
<!DOCTYPE html>
<html lang="en">
<head>
<meta charset="utf-8">
<title>Crestline Dentistry – Business Card</title>
<link rel="stylesheet" href="https://fonts.googleapis.com/css2?family=Open+Sans:wght@400;600&display=swap">
<style>
  :root {
    --page-bg: #1b1b1b;
    --card-bg: #0b0b0c;
    --card-edge: #2a2a2c;
    --band-bg: #060607;
    --band-line: #1e1e20;
    --cyan: #4cc9c4;
    --cyan-soft: #3fb3ae;
    --front-glow: #0f2a3a;
    --text-light: #d9dcdd;
    --text-muted: #8e9394;
  }
  * { box-sizing: border-box; margin: 0; padding: 0; }
  html, body {
    width: 1200px; height: 750px; overflow: hidden;
    background: var(--page-bg);
    font-family: "Open Sans", Arial, sans-serif;
  }
  .canvas { position: relative; width: 1200px; height: 750px; }

  .card {
    position: absolute;
    width: 570px; height: 360px;
    border-radius: 22px;
    background: var(--card-bg);
    border: 1px solid var(--card-edge);
    box-shadow: 0 10px 30px rgba(0,0,0,.6);
    overflow: hidden;
  }

  /* Back side: contact details */
  .card--back { left: 45px; top: 80px; }
  .contact-band {
    position: absolute; left: 0; right: 0; top: 150px; height: 82px;
    background: var(--band-bg);
    border-top: 1px solid var(--band-line);
    border-bottom: 1px solid var(--band-line);
    display: flex; align-items: center;
    padding-left: 40px;
  }
  .brand { display: flex; align-items: center; gap: 10px; width: 248px; }
  .brand__mark { width: 16px; height: 16px; background: var(--cyan); flex: none; }
  .brand__name { color: var(--cyan); font-size: 17px; font-weight: 400; line-height: 1.1; }
  .divider { width: 2px; height: 58px; background: var(--cyan); margin-right: 16px; }
  .doctor__name { color: var(--cyan); font-size: 22px; font-weight: 400; line-height: 1.1; }
  .doctor__degrees { color: var(--text-light); font-size: 13px; }
  .doctor__field { color: var(--text-muted); font-size: 8.5px; margin-top: 3px; }
  .doctor__contact { display: flex; gap: 22px; margin-top: 7px; color: var(--text-muted); font-size: 10px; }
  .contact-item { display: flex; align-items: center; gap: 7px; }
  .contact-item svg { fill: var(--text-muted); }

  /* Front side: brand */
  .card--front {
    left: 590px; top: 270px;
    background: radial-gradient(ellipse at 45% 50%, var(--front-glow) 0%, var(--card-bg) 70%);
    display: flex; align-items: center; justify-content: center;
  }
  .card--front .brand { width: auto; gap: 18px; }
  .card--front .brand__mark { width: 34px; height: 34px; }
  .card--front .brand__name { font-size: 40px; }
</style>
</head>
<body>
<main class="canvas">
  <section class="card card--back" aria-label="Card back">
    <div class="contact-band">
      <div class="brand">
        <span class="brand__mark"></span>
        <span class="brand__name">Crestline Dentistry</span>
      </div>
      <div class="divider"></div>
      <div class="doctor">
        <p class="doctor__name">Marcus Dorval <span class="doctor__degrees">(DDS, MMSc)</span></p>
        <p class="doctor__field">Smile Solutions/Prosthodontics/Implant Dentistry</p>
        <div class="doctor__contact">
          <span class="contact-item">
            <svg width="13" height="11" viewBox="0 0 13 11" aria-hidden="true"><path d="M1 3 C1 1 3 0 6.5 0 S12 1 12 3 L12 4 L9 4 L9 2.5 L4 2.5 L4 4 L1 4 Z M2 5 H11 L12 11 H1 Z"/></svg>
            000-000-0000
          </span>
          <span class="contact-item">
            <svg width="14" height="10" viewBox="0 0 14 10" aria-hidden="true"><path d="M0 0 H14 V10 H0 Z M1 1 L7 6 L13 1 Z" fill-rule="evenodd"/></svg>
            EMail@
          </span>
        </div>
      </div>
    </div>
  </section>

  <section class="card card--front" aria-label="Card front">
    <div class="brand">
      <span class="brand__mark"></span>
      <span class="brand__name">Crestline Dentistry</span>
    </div>
  </section>
</main>
</body>
</html>
```